Business Card Design Project - Tall Maple

We are looking for a new business card design. Our company name is Tall Maple Communication Solutions. Our primary function is to provide our clients with communication solutions. These solutions include commercial phone systems and T1 and Fiber Internet lines. Another major part of the business is cabling new buildings with CAT5 cable for both data and phone.

Industry/Entity Type

Communication

Requirements
Must have
• The cards need to be two sided and have some bleeding edge color.
Nice to have
• We are going to upload our current logo BUT we are not married to this logo. If you want to incorporate a re-designed logo with the new business card - please feel free to do so. We are looking for a new bold look that is very colorful yet professional.

```html
<!DOCTYPE html>
<html lang="en">
<head>
<meta charset="utf-8">
<title>Tall Maple Communication Solutions – Business Card</title>
<link rel="stylesheet" href="https://fonts.googleapis.com/css2?family=Source+Sans+3:wght@400;600&display=swap">
<style>
  :root {
    --navy: #26346a;
    --navy-deep: #1d2a58;
    --card-grey: #cdced0;
    --band-light: #e4e5e7;
    --ink: #5a5c60;
    --stage: #ececec;
    --white: #ffffff;
  }
  * { margin: 0; padding: 0; box-sizing: border-box; }
  html, body {
    width: 1200px; height: 800px; overflow: hidden;
    background: var(--stage);
    font-family: "Source Sans 3", "Helvetica Neue", Arial, sans-serif;
  }
  .card {
    position: absolute; left: 150px; top: 143px;
    width: 900px; height: 514px;
    background: var(--card-grey);
    box-shadow: 0 10px 30px rgba(0,0,0,.18);
    overflow: hidden;
  }
  .card-shapes { position: absolute; inset: 0; }
  .brand-name {
    position: absolute; left: 640px; top: 52px;
    color: var(--white); font-size: 34px; font-weight: 400;
    letter-spacing: .5px;
  }
  .contact {
    position: absolute; left: 70px; top: 190px;
    color: var(--ink);
  }
  .person-name { font-size: 40px; font-weight: 400; margin-bottom: 18px; }
  .phones { display: grid; grid-template-columns: 100px auto; font-size: 21px; line-height: 26px; }
  .company { margin-top: 26px; font-size: 21px; font-weight: 600; text-transform: uppercase; letter-spacing: .3px; }
  .address { font-size: 21px; line-height: 26px; }
</style>
</head>
<body>
  <div class="card">
    <svg class="card-shapes" width="900" height="514" viewBox="0 0 900 514">
      <rect x="0" y="0" width="420" height="60" fill="var(--band-light)"/>
      <rect x="0" y="0" width="360" height="30" fill="var(--navy)"/>
      <rect x="525" y="30" width="375" height="190" fill="var(--band-light)"/>
      <rect x="560" y="0" width="340" height="185" fill="var(--navy)"/>
      <circle class="faint-circle" cx="330" cy="235" r="115" fill="var(--white)" opacity=".22"/>
      <circle class="brand-circle" cx="560" cy="72" r="58" fill="var(--band-light)"/>
      <circle cx="560" cy="72" r="50" fill="var(--navy-deep)"/>
      <rect x="0" y="494" width="900" height="20" fill="var(--navy)"/>
    </svg>
    <div class="brand-name">Tall Maple</div>
    <div class="contact">
      <div class="person-name">Marcus Dellan</div>
      <div class="phones">
        <span>Office:</span><span>555.214.8830</span>
        <span>Cell:</span><span>555.309.4172</span>
        <span>24/7:</span><span>800.555.0148</span>
        <span>Fax:</span><span>800.555.0193</span>
      </div>
      <div class="company">Tall Maple Communication Solutions</div>
      <div class="address">1480 W Harbor Lane, Suite 210<br>Riverton, AZ 85099</div>
    </div>
  </div>
</body>
</html>
```